A Volume Worth Trading - book cover (front panel only)

I want a book cover (for print and ebook) in a distinctive, quirky style that can be repurposed for podcast artwork too. Full brief supplied.
The book is a practical, accessible handbook for anyone thinking about writing a book to build their business, with a wide range of tips and techniques to help plan, write, publishing and promote a book that’s integrated with your platform and works to build your reputation, network and credibility from day 1.
The target audience is experts in business, particularly owners of SMEs with an established online and offline platform (eg speaking, training, consulting) who want to add a book to take their business to the next level.
I want the design to be strong and distinctive, slightly quirky without being gimmicky, with the focus on typography.

Target Market(s)

Those writing a book based on their expertise to build their business

Industry/Entity Type

Publishing Company

Font styles to use
Serif
Sans Serif
Decorative

Colors

Designer to choose colors to be used in the design.

Requirements
Must have
• Commercially appealing book cover design, with application files and copyright supplied, front panel only, 5.5 x 8.5 inch format. Must work at both full size and thumbnail.
Nice to have
• A distinctive style that could be applied across other products in my portfolio.

```html
<!DOCTYPE html>
<html lang="en">
<head>
<meta charset="utf-8">
<title>A Volume Worth Trading – Front Cover</title>
<link href="https://fonts.googleapis.com/css2?family=Oswald:wght@400;500;700&family=Roboto:wght@500&display=swap" rel="stylesheet">
<style>
  :root {
    --backdrop: #f1f1f1;
    --cover-white: #ffffff;
    --title-red: #e21d1b;
    --ink: #1c1c1c;
    --rule: #2a2a2a;
    --art-warm: #f4c98a;
    --art-cool: #9fc6e6;
    --art-mid: #e9e9e9;
  }
  * { margin: 0; padding: 0; box-sizing: border-box; }
  html, body {
    width: 1200px;
    height: 1200px;
    overflow: hidden;
    background: var(--backdrop);
  }
  .canvas {
    position: relative;
    width: 1200px;
    height: 1200px;
  }
  .cover {
    position: absolute;
    left: 276px;
    top: 100px;
    width: 648px;
    height: 1000px;
    background: var(--cover-white);
    box-shadow: 0 0 0 1px #e2e2e2;
    text-align: center;
  }
  .cover-title { font-size: inherit; font-weight: inherit; }
  .title-line {
    position: absolute;
    left: 0;
    width: 100%;
    font-family: "Oswald", sans-serif;
    font-weight: 700;
    color: var(--title-red);
    text-transform: uppercase;
    line-height: 1;
    letter-spacing: 1px;
  }
  .title-top { top: 30px; font-size: 132px; }
  .title-bottom { top: 232px; font-size: 132px; }
  .title-link {
    position: absolute;
    top: 188px;
    left: 40px;
    right: 40px;
    display: flex;
    align-items: center;
    gap: 18px;
    font-family: "Oswald", sans-serif;
    font-weight: 700;
    font-size: 30px;
    color: var(--ink);
    text-transform: uppercase;
    letter-spacing: 1px;
  }
  .title-link::before,
  .title-link::after {
    content: "";
    flex: 1;
    height: 3px;
    background: var(--rule);
  }
  .subtitle {
    position: absolute;
    top: 408px;
    left: 40px;
    right: 40px;
    padding: 6px 0 8px;
    border-top: 2px solid var(--rule);
    border-bottom: 2px solid var(--rule);
    font-family: "Oswald", sans-serif;
    font-weight: 400;
    font-size: 24px;
    line-height: 1.15;
    color: var(--ink);
    text-transform: uppercase;
    letter-spacing: 0.5px;
  }
  .cover-art {
    position: absolute;
    top: 500px;
    left: 70px;
    width: 508px;
    height: 380px;
    border-radius: 50% 50% 30% 30% / 45% 45% 20% 20%;
    background:
      radial-gradient(circle at 30% 40%, var(--art-cool) 0%, transparent 45%),
      radial-gradient(circle at 72% 35%, var(--art-warm) 0%, transparent 45%),
      var(--art-mid);
  }
  .author {
    position: absolute;
    top: 910px;
    left: 0;
    width: 100%;
    font-family: "Roboto", sans-serif;
    font-weight: 500;
    font-size: 34px;
    letter-spacing: 2px;
    color: var(--ink);
    text-transform: uppercase;
  }
</style>
</head>
<body>
  <main class="canvas">
    <section class="cover">
      <h1 class="cover-title">
        <span class="title-line title-top">A Volume</span>
        <span class="title-link">Worth</span>
        <span class="title-line title-bottom">Trading</span>
      </h1>
      <p class="subtitle">Smart ways to shape and draft a book that<br>pulls its weight for your company</p>
      <div class="cover-art" role="img" aria-label="Sketched head in profile with gears, surrounded by doodled business icons, idea labels and coloured pencils"></div>
      <p class="author">Maren Holt</p>
    </section>
  </main>
</body>
</html>
```